Tallyden Web Design

Create Website Design for Tallyden. Tallyden is online application for collaboration team work system (task list management). More concept design for this project please find attach file ("tallyden website concept.pdf") . But my concept is just describe minimal features not bind design

For tallyden logo, i had already attach files. But i had not decided what color i chose, so it's okay if you suggest logo color for your suitable website design.
Updates

Dear All Designer,

I like brisk carousel (http://quillforge-labs.example/brisk-carousel/),
may be your concept design can adjust with this concept.
but don't worry about script for brisk carousel, my team will be handle
You just make website design to suitable with brisk carousel

but if you had own website design concept are welcome

thanks

Target Market(s)

Business Company

Industry/Entity Type

Management

```html
<!DOCTYPE html>
<html lang="en">
<head>
<meta charset="utf-8">
<title>Tallyden – Online Collaboration</title>
<link rel="stylesheet" href="https://fonts.googleapis.com/css2?family=Oswald:wght@300;400;500&family=Arimo:wght@400&display=swap">
<style>
  :root{
    --lime:#a4cf22;
    --leaf:#5f9a1c;
    --leaf-dark:#4f8415;
    --footer:#5f8d24;
    --teal:#1f4c55;
    --nav-ink:#2b4c4f;
    --body-ink:#6a6f72;
    --white:#ffffff;
    --card-bg:rgba(255,255,255,0.42);
    --card-line:rgba(255,255,255,0.55);
  }
  *{box-sizing:border-box;margin:0;padding:0}
  html,body{width:1200px;height:1195px;overflow:hidden;background:var(--white)}
  body{position:relative;font-family:"Arimo",Arial,sans-serif}
  .display{font-family:"Oswald","Arial Narrow",sans-serif}

  /* header */
  .site-header{position:absolute;left:0;top:0;width:1200px;height:118px;background:var(--white)}
  .brand{position:absolute;left:162px;top:22px;display:flex;align-items:center;gap:12px}
  .brand-name{font-family:"Oswald","Arial Narrow",sans-serif;font-weight:400;font-size:60px;line-height:1;color:var(--teal)}
  .brand-dot{width:26px;height:26px;border-radius:50%;background:var(--lime)}
  .main-nav{position:absolute;left:516px;top:0;width:684px;height:118px;background:var(--lime)}
  .main-nav a{position:absolute;top:70px;font-family:"Oswald","Arial Narrow",sans-serif;font-size:16px;font-weight:400;color:var(--nav-ink);text-decoration:none;letter-spacing:-0.2px}

  /* hero */
  .hero{position:absolute;left:0;top:118px;width:1200px;height:647px;
    background:
      radial-gradient(ellipse 300px 220px at 150px 380px, rgba(214,170,150,0.8), transparent 70%),
      radial-gradient(ellipse 360px 260px at 1050px 150px, rgba(120,130,150,0.8), transparent 70%),
      radial-gradient(ellipse 420px 260px at 620px 560px, rgba(225,195,175,0.85), transparent 70%),
      linear-gradient(160deg,#4e5a7a 0%,#7b7f98 35%,#b39a98 65%,#d9bfb0 100%);}
  .slide-back{position:absolute;top:47px;width:58px;height:264px;background:var(--white);box-shadow:0 2px 6px rgba(0,0,0,0.3)}
  .slide-back .fill{position:absolute;inset:8px;background:linear-gradient(90deg,#e6b58a,#c98c5a)}
  .slide-frame{position:absolute;left:192px;top:31px;width:451px;height:295px;background:var(--white);box-shadow:0 3px 10px rgba(0,0,0,0.35)}
  .slide-photo{position:absolute;left:9px;top:9px;width:433px;height:277px;background:linear-gradient(135deg,#cfe07a 0%,#8fbf3a 45%,#4f8a22 100%)}
  .slider-dots{position:absolute;left:385px;top:351px;display:flex;gap:8px}
  .slider-dots span{width:10px;height:10px;border-radius:2px;background:var(--white)}
  .slider-dots span.active{background:#3d3d3d}
  .headline{position:absolute;left:718px;top:42px;color:var(--white);text-transform:uppercase}
  .headline .l1{font-size:76px;line-height:76px;font-weight:400;letter-spacing:-1px}
  .headline .l2{font-size:36px;line-height:40px;font-weight:400;letter-spacing:-0.5px}
  .headline .l3{font-size:46px;line-height:54px;font-weight:400;letter-spacing:-0.5px}

  /* feature cards */
  .feature-card{position:absolute;width:277px;height:102px;background:var(--card-bg);border:1px solid var(--card-line)}
  .feature-icon{position:absolute;left:12px;top:18px;width:62px;height:62px;border-radius:6px;background:linear-gradient(160deg,#e7eef5,#9fb2c6)}
  .feature-card::before{content:"";position:absolute;left:88px;top:0;width:1px;height:100%;background:var(--card-line)}
  .feature-title{position:absolute;left:103px;top:9px;font-size:19px;font-weight:400;color:var(--teal);letter-spacing:-0.2px}
  .feature-text{position:absolute;left:104px;top:40px;width:153px;font-size:10px;line-height:13px;color:#3d3d3d;text-align:justify}
  .btn{display:inline-block;background:var(--leaf);color:var(--white);font-family:"Oswald","Arial Narrow",sans-serif;text-decoration:none;text-align:center;box-shadow:inset 0 1px 0 rgba(255,255,255,0.25)}
  .feature-card .btn{position:absolute;left:105px;top:71px;width:70px;height:20px;font-size:11px;line-height:20px}

  /* about */
  .about-media{position:absolute;left:162px;top:784px;width:428px;height:303px;background:linear-gradient(120deg,#3e6fc0 0%,#8aa4d0 35%,#e4b6a4 60%,#d0457f 100%)}
  .play{position:absolute;left:330px;top:106px}
  .about-title{position:absolute;left:611px;top:776px;font-size:32px;font-weight:400;color:var(--teal);letter-spacing:-0.3px}
  .about-text{position:absolute;left:611px;width:428px;font-size:12.2px;line-height:14.8px;color:var(--body-ink);text-align:justify}
  .about-btn{position:absolute;left:611px;top:1050px;width:117px;height:37px;font-size:18px;line-height:37px}

  /* footer */
  .site-footer{position:absolute;left:0;top:1104px;width:1200px;height:91px;background:var(--footer)}
  .site-footer::before{content:"";position:absolute;left:0;top:-4px;width:100%;height:8px;
    background:radial-gradient(circle at 4px 4px,var(--footer) 3.5px,transparent 4px) 0 0/8px 8px repeat-x}
  .footer-links{position:absolute;left:162px;top:21px;font-size:11.5px;color:var(--white)}
  .footer-links a{color:var(--white);text-decoration:none}
  .footer-links .sep{margin:0 4px}
  .copyright{position:absolute;left:162px;top:38px;font-size:11.5px;color:var(--white)}
  .follow{position:absolute;left:796px;top:32px;font-size:15px;color:var(--white);letter-spacing:-0.3px}
  .social{position:absolute;left:893px;top:25px;display:flex;gap:7px}
  .social span{width:26px;height:26px;border-radius:50%;background:#f4f6f2;box-shadow:0 1px 2px rgba(0,0,0,0.3)}
</style>
</head>
<body>

<header class="site-header">
  <div class="brand"><span class="brand-name">tallyden</span><span class="brand-dot"></span></div>
  <nav class="main-nav">
    <a href="#" style="left:33px">HOME</a>
    <a href="#" style="left:102px">PRODUCTS</a>
    <a href="#" style="left:197px">SOLUTIONS</a>
    <a href="#" style="left:297px">INDUSTRIES</a>
    <a href="#" style="left:399px">ABOUT US</a>
    <a href="#" style="left:492px">LOGIN</a>
  </nav>
</header>

<section class="hero" role="img" aria-label="Soft blurred background photo of people working together">
  <div class="slide-back" style="left:164px"><div class="fill"></div></div>
  <div class="slide-back" style="left:612px"><div class="fill"></div></div>
  <div class="slide-frame">
    <div class="slide-photo" role="img" aria-label="Carousel photo: woman lying in green grass using a tablet"></div>
  </div>
  <div class="slider-dots"><span></span><span class="active"></span><span></span><span></span></div>

  <h1 class="headline display">
    <div class="l1">Customize</div>
    <div class="l2">Online Collaboration</div>
    <div class="l3">Team Work</div>
  </h1>

  <div class="feature-card" style="left:163px;top:394px">
    <div class="feature-icon" role="img" aria-label="Application icon"></div>
    <h3 class="feature-title display">Customize Application</h3>
    <p class="feature-text">Lorem ipsum dolor sit amet, sectetuer adipiscing elit.</p>
    <a class="btn" href="#">View More</a>
  </div>
  <div class="feature-card" style="left:463px;top:394px">
    <div class="feature-icon" role="img" aria-label="Application icon"></div>
    <h3 class="feature-title display">Customize Application</h3>
    <p class="feature-text">Lorem ipsum dolor sit amet, sectetuer adipiscing elit.</p>
    <a class="btn" href="#">View More</a>
  </div>
  <div class="feature-card" style="left:763px;top:394px">
    <div class="feature-icon" role="img" aria-label="Application icon"></div>
    <h3 class="feature-title display">Customize Application</h3>
    <p class="feature-text">Lorem ipsum dolor sit amet, sectetuer adipiscing elit.</p>
    <a class="btn" href="#">View More</a>
  </div>
  <div class="feature-card" style="left:163px;top:520px">
    <div class="feature-icon" role="img" aria-label="Application icon"></div>
    <h3 class="feature-title display">Customize Application</h3>
    <p class="feature-text">Lorem ipsum dolor sit amet, sectetuer adipiscing elit.</p>
    <a class="btn" href="#">View More</a>
  </div>
  <div class="feature-card" style="left:463px;top:520px">
    <div class="feature-icon" role="img" aria-label="Application icon"></div>
    <h3 class="feature-title display">Customize Application</h3>
    <p class="feature-text">Lorem ipsum dolor sit amet, sectetuer adipiscing elit.</p>
    <a class="btn" href="#">View More</a>
  </div>
  <div class="feature-card" style="left:763px;top:520px">
    <div class="feature-icon" role="img" aria-label="Application icon"></div>
    <h3 class="feature-title display">Customize Application</h3>
    <p class="feature-text">Lorem ipsum dolor sit amet, sectetuer adipiscing elit.</p>
    <a class="btn" href="#">View More</a>
  </div>
</section>

<section>
  <div class="about-media" role="img" aria-label="Video still: students with a book and a phone">
    <svg class="play" width="92" height="92" viewBox="0 0 92 92" aria-hidden="true">
      <circle cx="46" cy="46" r="46" fill="rgba(90,90,95,0.75)"/>
      <path d="M33 24 L70 46 L33 68 Z" fill="#ffffff"/>
    </svg>
  </div>
  <h2 class="about-title display">ABOUT TALLYDEN</h2>
  <p class="about-text" style="top:832px">Lorem ipsum dolor sit amet, consectetuer adipiscing elit. Aenean commodo ligula eget dolor. Aenean massa. Cum sociis natoque penatibus et magnis dis parturient montes, nascetur ridiculus mus. Donec quam felis, ultricies nec, pellentesque eu, pretium quis, sem. Nulla consequat massa quis enim.</p>
  <p class="about-text" style="top:921px">Donec pede justo, fringilla vel, aliquet nec, vulputate eget, arcu. In enim justo, rhoncus ut, imperdiet a, venenatis vitae, justo. Nullam dictum felis eu pede mollis pretium. Integer tincidunt. Cras dapibus. Vivamus elementum semper nisi. Aenean vulputate eleifend tellus.Lorem ipsum dolor sit amet, consectetuer adipiscing elit. Aenean commodo ligula eget dolor. Aenean massa. Cum sociis natoque penatibus et magnis dis parturient montes,</p>
  <a class="btn about-btn" href="#">View More</a>
</section>

<footer class="site-footer">
  <nav class="footer-links">
    <a href="#">Home</a><span class="sep">|</span><a href="#">About Us</a><span class="sep">|</span><a href="#">Careers</a><span class="sep">|</span><a href="#">Terms &amp; Conditions</a><span class="sep">|</span><a href="#">Contact</a>
  </nav>
  <p class="copyright">Copyright © 2012. All Rights Reserved.</p>
  <p class="follow display">FOLLOW US ON</p>
  <div class="social"><span></span><span></span><span></span><span></span></div>
</footer>

</body>
</html>
```